Poster Design Project

We are a pizzeria based in Sydney CBD. Please see attached file for new website, do not use the current website look to make your graphic design.

We want to run a promotional campaign called " Crust Carnival".

Crust Carnival
$9 Pizza

Crispy & fresh dough topped with mouth watering mozzarella cheese, sprinkled with oregano and finished with fresh basil.

takeaway & eat in only
Medium Pizza Only (11 inch)

Target Market(s)

It is the lunch crowd in sydney cbd, predominately male but some female too. targeting the office workers.

Industry/Entity Type

Graphic Design

Requirements
Must have
• We are an Italian Pizzeria, so we would like an italian look and feel
our unique advantage is authentic and delicious thin crispy pizza
we want a nostalgic look and feel
some examples are attached of colours and style we like
Nice to have
• I can send you via email files to show you what the new website will look like

```html
<!DOCTYPE html>
<html lang="en">
<head>
<meta charset="utf-8">
<title>Crust Carnival – $9 Pizza</title>
<link rel="stylesheet" href="https://fonts.googleapis.com/css2?family=Playfair+Display:ital,wght@1,900&family=Lora:ital,wght@1,700&family=Kaushan+Script&family=Anton&family=Oswald:wght@600&display=swap">
<style>
  :root {
    --flag-red: #c0202f;
    --ribbon-red: #e2232f;
    --deep-red: #9e1424;
    --flag-green: #1d8a3c;
    --title-green: #1c9a3f;
    --outline-green: #138a35;
    --cream: #f1ead6;
    --gold: #f2c21b;
    --ink: #111111;
    --pale-cream: #f4f0d8;
    --white: #ffffff;
  }
  * { margin: 0; padding: 0; box-sizing: border-box; }
  html, body { width: 848px; height: 1200px; overflow: hidden; background: #ffffff; }
  .poster {
    position: relative;
    width: 848px;
    height: 1200px;
    overflow: hidden;
    background: var(--cream);
  }
  .band-red {
    position: absolute; left: 0; top: 0; width: 100%; height: 335px;
    background: linear-gradient(120deg, #d2303d 0%, var(--flag-red) 45%, #b01b2a 100%);
  }
  .pizza-photo {
    position: absolute; left: 0; top: 335px; width: 100%; height: 665px;
    background:
      radial-gradient(ellipse at 20% 30%, rgba(120,150,90,.55), transparent 45%),
      radial-gradient(ellipse at 75% 70%, rgba(120,140,80,.5), transparent 40%),
      radial-gradient(ellipse at 50% 55%, rgba(240,210,140,.9), transparent 60%),
      linear-gradient(180deg, #e6dcc0 0%, #e9cf9a 40%, #dcb57a 75%, #e8dcc0 100%);
  }
  .band-green {
    position: absolute; left: 0; top: 1000px; width: 100%; height: 200px;
    background: linear-gradient(100deg, #17793a 0%, var(--flag-green) 60%, #27a04a 100%);
  }
  .ribbon { position: absolute; left: 0; top: 0; width: 848px; height: 1200px; }
  .headline { margin: 0; }
  .title {
    position: absolute;
    display: block;
    font-family: "Playfair Display", Georgia, serif;
    font-style: italic;
    font-weight: 900;
    letter-spacing: -1px;
    -webkit-text-stroke: 12px var(--white);
    paint-order: stroke fill;
    line-height: 1;
    white-space: nowrap;
    transform: rotate(-5deg);
    transform-origin: left bottom;
  }
  .title-line1 {
    left: 150px; top: 175px; font-size: 150px;
    color: var(--title-green);
    filter:
      drop-shadow(4px 0 0 var(--deep-red)) drop-shadow(-4px 0 0 var(--deep-red))
      drop-shadow(0 4px 0 var(--deep-red)) drop-shadow(0 -4px 0 var(--deep-red));
  }
  .title-line2 {
    left: 100px; top: 345px; font-size: 122px;
    color: var(--ribbon-red);
    filter:
      drop-shadow(5px 0 0 var(--outline-green)) drop-shadow(-5px 0 0 var(--outline-green))
      drop-shadow(0 5px 0 var(--outline-green)) drop-shadow(0 -5px 0 var(--outline-green));
  }
  .price-badge { position: absolute; left: 0; top: 0; width: 848px; height: 1200px; }
  .price {
    position: absolute; left: 600px; top: 478px;
    font-family: "Anton", Impact, sans-serif;
    font-size: 84px; line-height: 1;
    color: var(--title-green);
    -webkit-text-stroke: 3px var(--white); paint-order: stroke fill;
  }
  .price-label {
    position: absolute; left: 510px; top: 560px;
    font-family: "Kaushan Script", cursive;
    font-size: 104px; line-height: 1;
    color: var(--ribbon-red);
    -webkit-text-stroke: 8px var(--white); paint-order: stroke fill;
    filter:
      drop-shadow(4px 0 0 var(--outline-green)) drop-shadow(-4px 0 0 var(--outline-green))
      drop-shadow(0 4px 0 var(--outline-green)) drop-shadow(0 -4px 0 var(--outline-green));
    transform: rotate(-8deg);
  }
  .description {
    position: absolute; left: 68px; top: 698px;
    font-family: "Lora", Georgia, serif;
    font-style: italic; font-weight: 700;
    font-size: 31px; line-height: 33px;
    letter-spacing: 3.5px;
    color: var(--ink);
    text-shadow: 0 0 6px rgba(255,255,255,.7);
    white-space: nowrap;
  }
  .service {
    position: absolute; left: 0; top: 914px; width: 100%;
    text-align: center;
    font-family: "Anton", Impact, sans-serif;
    font-size: 64px; line-height: 1;
    color: var(--ink);
  }
  .size-note {
    position: absolute; left: 0; top: 1022px; width: 100%;
    text-align: center;
    font-family: "Oswald", Arial, sans-serif;
    font-weight: 600; font-size: 29px;
    color: var(--pale-cream);
  }
</style>
</head>
<body>
<main class="poster">
  <div class="band-red"></div>
  <div class="pizza-photo" role="img" aria-label="Close-up photograph of a margherita pizza with melted mozzarella, tomato and fresh basil leaves"></div>
  <div class="band-green"></div>

  <svg class="ribbon" viewBox="0 0 848 1200" aria-hidden="true">
    <polygon points="95,445 775,285 775,380 95,555" fill="var(--ribbon-red)"/>
    <polygon points="95,460 775,300 775,306 95,466" fill="var(--gold)"/>
    <polygon points="95,534 775,358 775,364 95,540" fill="var(--gold)"/>
  </svg>

  <h1 class="headline">
    <span class="title title-line1">Crust</span>
    <span class="title title-line2">Carnival</span>
  </h1>

  <svg class="price-badge" viewBox="0 0 848 1200" aria-hidden="true">
    <polygon fill="var(--gold)" stroke="var(--ribbon-red)" stroke-width="3"
      points="780,545 762,565 771,591 746,603 745,630 718,631 706,656 680,647 660,665 640,647 614,656 602,631 575,630 574,603 549,591 558,565 540,545 558,525 549,499 574,487 575,460 602,459 614,434 640,443 660,425 680,443 706,434 718,459 745,460 746,487 771,499 762,525"/>
    <circle cx="660" cy="545" r="88" fill="var(--ribbon-red)"/>
    <circle cx="660" cy="545" r="78" fill="var(--cream)" stroke="var(--gold)" stroke-width="4" stroke-dasharray="4 6"/>
  </svg>
  <div class="price">$9</div>
  <div class="price-label">Pizza</div>

  <p class="description">Crispy &amp; fresh dough topped<br>with mouth watering mozzarella cheese,<br>sprinkled with oregano<br>and finished with fresh basil.</p>

  <p class="service">takeaway &amp; eat in only</p>
  <p class="size-note">Medium Pizza Only (11 inch)</p>
</main>
</body>
</html>
```